Health - Still Meadow Project

I am running a new Still Meadow Conference that will have meditation, mediums and healers - this is a first time conference. However the conference is aimed at mainstream 'normal' people. The 'normal' people, don't want to hear or see words like Tantra, Prana, Angels, etc, but they have problems that can be alleviated through these mediums. The design should communicate light, soothing, comforting, healing. I would like a web design for a single page that can be used as a landing page for the conference registration. I also need a logo and a flyer that can be made into posters A4 or A3 posters. I need to be able to edit all documents as there will be changes in the program through time. I have attached the initial agenda. This conference will be held in Victoria, Australia.
Target Market(s)
Mums and grandmas
Industry/Entity Type
Health And Wellness
Number of Pages Required
1 page

```html
<!DOCTYPE html>
<html lang="en">
<head>
<meta charset="utf-8">
<title>Still Meadow Conference</title>
<link rel="stylesheet" href="https://fonts.googleapis.com/css2?family=Tinos:wght@400;700&family=Open+Sans:wght@400;600&display=swap">
<style>
:root{
  --blue:#2a9fe0;
  --blue-dark:#1f8fd0;
  --ink:#3d3d3d;
  --muted:#5a5a5a;
  --panel:#f1f1f1;
  --bar:#e1e1e1;
  --footer:#2f3439;
  --footer-line:#6a6f74;
  --white:#ffffff;
}
*{margin:0;padding:0;box-sizing:border-box}
html,body{width:1200px;height:3871px;overflow:hidden}
body{font-family:"Open Sans",Arial,sans-serif;color:var(--ink);background:var(--white);position:relative}
.section{position:absolute;left:0;width:1200px;overflow:hidden}
.serif{font-family:"Tinos","Times New Roman",serif}
.btn{position:absolute;display:flex;align-items:center;justify-content:center;gap:14px;width:192px;height:40px;background:var(--blue);color:var(--white);font-size:16px;font-weight:600;border-radius:2px}
.btn svg{width:9px;height:14px}
.center-x{left:50%;transform:translateX(-50%)}

/* hero */
.hero{top:0;height:560px;background:linear-gradient(180deg,#2a3442 0%,#39434f 38%,#7a6a58 60%,#c58a48 66%,#5b5450 74%,#2b2e33 100%)}
.hero-photo{position:absolute;inset:0}
.topbar{position:absolute;top:20px;left:130px;right:130px;height:48px;display:flex;align-items:center;justify-content:space-between;color:var(--white)}
.brand{display:flex;align-items:center;gap:12px;font-family:"Tinos",serif;font-size:26px}
.brand-dot{width:34px;height:34px;border-radius:50%;background:var(--blue)}
.contact-top{display:flex;align-items:center;gap:26px;font-size:15px}
.contact-top span{display:flex;align-items:center;gap:8px}
.contact-top svg{width:15px;height:15px}
.hero h1{position:absolute;top:220px;width:100%;text-align:center;color:var(--white);font-weight:400;font-size:46px;line-height:56px}
.hero .btn{top:352px}

/* intro */
.intro{top:560px;height:410px;background:var(--white)}
.intro-photo{position:absolute;right:0;top:20px;width:425px;height:390px;background:radial-gradient(ellipse at 60% 40%,#ffffff 0%,#dfeef8 45%,#8cc7e8 80%,#4aa6d8 100%)}
.intro h2{position:absolute;left:130px;top:30px;font-size:36px;color:var(--blue);font-weight:400}
.intro .date{position:absolute;left:130px;top:80px;font-size:21px;color:var(--muted)}
.intro .copy{position:absolute;left:130px;top:135px;width:625px;font-size:13px;line-height:23px;color:var(--muted)}
.intro .copy p+p{margin-top:16px}

/* bands */
.band{background:linear-gradient(180deg,#1c2535 0%,#2a3850 45%,#3a4150 62%,#1a1f2a 100%)}
.band-hope{top:970px;height:423px}
.band-hope .l1{position:absolute;top:80px;width:100%;text-align:center;color:var(--white);font-size:34px}
.band-hope .l2{position:absolute;top:138px;width:100%;text-align:center;color:var(--blue);font-size:48px}
.band-hope .l3{position:absolute;top:205px;width:100%;text-align:center;color:#e6e6e6;font-size:32px}
.band-hope .btn{top:293px}
.band-paradise{top:2224px;height:330px}
.band-paradise .l1{position:absolute;top:95px;width:100%;text-align:center;color:var(--blue);font-size:42px}
.band-paradise .l2{position:absolute;top:148px;width:100%;text-align:center;color:#e6e6e6;font-size:31px}
.band-paradise .btn{top:228px}

/* sessions */
.session{background:var(--white)}
.session.alt{background:var(--panel)}
.portrait{position:absolute;width:216px;height:278px;box-shadow:0 4px 10px rgba(0,0,0,.3)}
.session h3{position:absolute;font-size:29px;color:var(--blue);font-weight:400}
.session .copy{position:absolute;font-size:13.5px;line-height:23px;color:var(--muted)}
.session .copy p+p{margin-top:18px}
.facilitator{position:absolute;height:42px;width:540px;background:var(--bar);display:flex;align-items:center;padding-left:24px;font-size:19px;color:var(--ink)}
.facilitator i{font-style:normal;margin:0 14px}

.s1{top:1393px;height:413px}
.s2{top:1806px;height:418px}
.s3{top:2554px;height:516px}
.s4{top:3070px;height:367px}

/* footer */
.footer{top:3437px;height:434px;background:var(--footer);color:var(--white)}
.footer h4{position:absolute;top:50px;font-size:27px;color:var(--blue);font-weight:400}
.footer h4::after{content:"";position:absolute;left:0;top:46px;height:2px;background:var(--footer-line)}
.reg h4::after{width:594px}
.contact h4::after{width:294px}
.reg h4{left:130px}
.contact h4{left:776px}
.field{position:absolute;font-size:14px;color:#e8e8e8;border-bottom:2px solid var(--footer-line);padding-bottom:8px}
.submit{position:absolute;left:130px;top:286px;width:154px;height:38px;background:var(--blue);color:var(--white);font-size:16px;font-weight:600;display:flex;align-items:center;justify-content:center;border-radius:2px}
.contact-list{position:absolute;left:776px;top:135px;width:300px;font-size:13px;line-height:20px;color:#e8e8e8;list-style:none}
.contact-list li{display:flex;gap:12px;margin-bottom:16px}
.contact-list svg{flex:none;width:13px;height:13px;margin-top:4px}
.social{position:absolute;left:776px;top:277px;display:flex;gap:12px}
.social span{width:28px;height:28px;background:var(--blue-dark);border-radius:2px}
.footer-rule{position:absolute;left:130px;right:130px;top:363px;height:1px;background:#454a50}
.copyright{position:absolute;top:388px;width:100%;text-align:center;font-size:13px;color:#d6d6d6}
</style>
</head>
<body>

<section class="section hero">
  <div class="hero-photo" role="img" aria-label="Silhouette of a person meditating by the sea at sunset"></div>
  <header class="topbar">
    <div class="brand"><span class="brand-dot"></span>Still Meadow</div>
    <div class="contact-top">
      <span><svg viewBox="0 0 16 16"><path fill="#2a9fe0" d="M3.6 1.2l2.3 2.4-1.3 1.9c.8 1.8 2.2 3.2 4 4l1.9-1.3 2.4 2.3-1.4 2.6C6.4 13 2.9 9.6 1 4.5z"/></svg>Call Us &nbsp;555-0142-7730</span>
      <span style="opacity:.8">|</span>
      <span><svg viewBox="0 0 16 16"><rect x="1" y="3" width="14" height="10" fill="#2a9fe0"/><path d="M1 3l7 6 7-6" stroke="#fff" fill="none"/></svg>Email: info@stillmeadow.com</span>
    </div>
  </header>
  <h1 class="serif">Experience an<br>Awakening Discover HOPE!</h1>
  <div class="btn center-x">Register Now! <svg viewBox="0 0 9 14"><path d="M1 1l6 6-6 6" stroke="#fff" stroke-width="2" fill="none"/></svg></div>
</section>

<section class="section intro">
  <div class="intro-photo" role="img" aria-label="Smiling woman in a blue top raising her arms against a bright sky"></div>
  <h2 class="serif">Still Meadow Conference</h2>
  <div class="date">Saturday August 20th 2016</div>
  <div class="copy">
    <p>Sed ut perspiciatis unde omnis iste natus error sit voluptatem accusantium doloremque laudantium, totam rem aperiam, eaque ipsa quae ab illo inventore veritatis et quasi architecto beatae vitae dicta sunt explicabo. Nemo enim ipsam voluptatem quia voluptas sit aspernatur aut odit aut fugit. Sed ut perspiciatis unde omnis iste natus error sit voluptatem accusantium doloremque laudantium, totam rem aperiam, eaque ipsa quae ab illo inventore veritatis et quasi architecto beatae vitae dicta sunt explicabo.</p>
    <p>Nemo enim ipsam voluptatem quia voluptas sit aspernatur aut odit aut fugit. Sed ut perspiciatis unde omnis iste natus error sit voluptatem accusantium doloremque laudantium, totam</p>
  </div>
</section>

<section class="section band band-hope" role="img" aria-label="City skyline at night reflected on the river">
  <div class="l1 serif">Discover Hope Start Your Recovery Today</div>
  <div class="l2 serif">Meditation, Mediums &amp; Healers.</div>
  <div class="l3 serif">Help you solved your problems</div>
  <div class="btn center-x">Register Now! <svg viewBox="0 0 9 14"><path d="M1 1l6 6-6 6" stroke="#fff" stroke-width="2" fill="none"/></svg></div>
</section>

<section class="section session s1">
  <div class="portrait" style="left:130px;top:44px;background:linear-gradient(160deg,#8dc9e6,#6fb2d6)" role="img" aria-label="Portrait of facilitator Maren Holloway"></div>
  <h3 class="serif" style="left:385px;top:50px">Wild Hairs – Embarking Upon the Spiritual Life</h3>
  <div class="copy" style="left:385px;top:100px;width:685px">
    <p>Everyone is searching for love, joy and peace – aren't we? Yet love, joy and peace is already our natural state of being. So how did we come to forget this fundamental Truth? Why are we searching for what we already are? The answers to these questions are rather simple and obvious, but only after we come to understand the nature of the human ego. For too long, the human ego has taken us on a wild goose chase.</p>
    <p>It could take an entire lifetime of study, to fully grasp the magnitude of the nature of awakening. In this discussion you will receive a very simple to understand explanation of the journey humanity is undertaking, from conception to enlightenment – and how you can assess where you are on your own journey and keys to unlocking your love, joy and peace.</p>
  </div>
  <div class="facilitator serif" style="left:385px;top:333px">Facilitator: Maren Holloway <i>|</i> (9:00am – 10:45am)</div>
</section>

<section class="section session alt s2">
  <h3 class="serif" style="left:130px;top:40px">Conscious Connection &amp; Living Life Fully</h3>
  <div class="copy" style="left:130px;top:95px;width:690px">
    <p>We live in a world where most people feel disconnected or 'out of synch' with friends, loved ones and the daily experiences we share with one another. This workshop is designed to offer you a framework for LIVING more consciously, intimately and with greater connection, presence and depth – to ourselves and others. The more we feel connected to ourselves, the more connected we will feel with others. In a time where more and more people are feeling isolated in a busy urban existence, simple practices can foster love, connection and fulfillment. Come &amp; explore simple, facilitated exercises that deepen a heart-felt, authentic and feeling space.</p>
  </div>
  <div class="facilitator serif" style="left:130px;top:294px">Facilitator: Tess Adair <i>|</i> (11:00am – 12:45pm)</div>
  <div class="portrait" style="left:849px;top:44px;background:linear-gradient(160deg,#ecdcc0,#b59a78)" role="img" aria-label="Portrait of facilitator Tess Adair"></div>
</section>

<section class="section band band-paradise" role="img" aria-label="Harbour city skyline at dusk">
  <div class="l1 serif">Achieve Your Recovery And Sobriety In Paradise</div>
  <div class="l2 serif">Conference Will Be Held In Australia</div>
  <div class="btn center-x">Register Now! <svg viewBox="0 0 9 14"><path d="M1 1l6 6-6 6" stroke="#fff" stroke-width="2" fill="none"/></svg></div>
</section>

<section class="section session s3">
  <div class="portrait" style="left:130px;top:75px;background:linear-gradient(160deg,#e9e9e9,#c6c6c6)" role="img" aria-label="Portrait of facilitator Owen Carrick"></div>
  <h3 class="serif" style="left:385px;top:80px">He Slow Breath to Freedom</h3>
  <div class="copy" style="left:385px;top:130px;width:685px">
    <p>Stress is is one of the number one causes of leading diseases today. The connection between Mind and Body has long since been established by both science and spirituality. This session will guide you through simple meditations, self-inquiry, mindful eating and movement. You will find these tools extremely useful to releasing the stress valve, improving your relationships and managing your day to day life in a more enjoyable, present way.</p>
    <p>Using his highly intuitive skills and the "Open Heart Practice" Owen will help you experience your divine nature and harness your individual power – enabling you to live a life in harmony and peace.</p>
    <p>Working largely through breathing, focusing and self-inquiry techniques Owen has discovered we can all be transformed. These approaches help people break through old limiting patterns of behaviour, helping them to make healthy and positive change in their lives.</p>
  </div>
  <div class="facilitator serif" style="left:385px;top:431px">Facilitator: Owen Carrick <i>|</i> (1:30pm – 3:15pm)</div>
</section>

<section class="section session alt s4">
  <h3 class="serif" style="left:130px;top:40px">Learning to SHINE</h3>
  <div class="copy" style="left:130px;top:92px;width:690px">
    <p>In a world where too often we feel less than our bright, shiny best we can all afford to bring out more of our own natural light to shine for ourselves and others. In this session, Nina will guide you through ways to connect with your inner SHINE and not only use that to brighten yourself, but to shine your light on others to share in warmth and love that improves all things.</p>
  </div>
  <div class="facilitator serif" style="left:130px;top:227px">Facilitator: Nina Barlow <i>|</i> (3:30pm – 5:00pm)</div>
  <div class="portrait" style="left:849px;top:44px;background:linear-gradient(160deg,#b9d6ea,#7a8f7a)" role="img" aria-label="Portrait of facilitator Nina Barlow"></div>
</section>

<footer class="section footer">
  <div class="reg"><h4 class="serif">Register Now</h4></div>
  <div class="field" style="left:130px;top:130px;width:288px">First Name</div>
  <div class="field" style="left:440px;top:130px;width:284px">Last Name</div>
  <div class="field" style="left:130px;top:180px;width:288px">E-mail</div>
  <div class="field" style="left:440px;top:180px;width:284px">Phone</div>
  <div class="field" style="left:130px;top:224px;width:594px">Your Message</div>
  <div class="submit">Submit</div>

  <div class="contact"><h4 class="serif">Contact us</h4></div>
  <ul class="contact-list">
    <li><svg viewBox="0 0 12 12"><path fill="#2a9fe0" d="M6 0a4 4 0 0 0-4 4c0 3 4 8 4 8s4-5 4-8a4 4 0 0 0-4-4zm0 5.5A1.5 1.5 0 1 1 6 2.5a1.5 1.5 0 0 1 0 3z"/></svg><span>14 Willow Lane, Fernvale Grove VIC 3999 Australia</span></li>
    <li><svg viewBox="0 0 16 16"><path fill="#2a9fe0" d="M3.6 1.2l2.3 2.4-1.3 1.9c.8 1.8 2.2 3.2 4 4l1.9-1.3 2.4 2.3-1.4 2.6C6.4 13 2.9 9.6 1 4.5z"/></svg><span>Phone: +555 014 2773</span></li>
    <li><svg viewBox="0 0 16 16"><rect x="1" y="3" width="14" height="10" fill="#2a9fe0"/><path d="M1 3l7 6 7-6" stroke="#2f3439" fill="none"/></svg><span>Email: info@stillmeadow.com</span></li>
  </ul>
  <div class="social" aria-label="Social links"><span></span><span></span><span></span><span></span></div>

  <div class="footer-rule"></div>
  <div class="copyright">Copyright © 2016 Still Meadow. All Rights Reserved</div>
</footer>

</body>
</html>
```